Designer and consultant for professionals/businesses and manufacturers in the kitchen and bath in...

I have 30 years of design experience, and 19 of those years within the marketing team of a national cabinet manufacturer. This role gave me the opportunity to consult and design for kitchen/bath businesses, from boutique to multi-store national scale. My services include layout and spatial planning, individual display design, and product design for cabinet manufacturers. From showrooms, to trade shows to integrated design collections. I would like to see designs that convey professionalism, as well as an appeal to the creative designer mind!

Target Market(s)

Kitchen and bath dealers, as well as mid-scale multi-store home centers. Cabinet manufacturers, Trade Show agencies.

Industry/Entity Type

Kitchen

Contact Information for Business Card

Serving Kitchen and Bath Businesses

Logo Text

MT (initials for business name)

Font styles to use
Serif
Sans Serif
Decorative

Colors
e34197

Requirements
Must have
• Marlowe Tenbury Design and Consulting, Inc. (business name)
• marlowe@mtvorplan.com (email)
• 608-241-7789 (phone)
• mtvorplan.com (website)
Nice to have
• Inclusions of geometric shapes; particularly a 30/15 degree triangle and circle(s)
• 2 colors
Should not have
• Not too artsy!

```html
<!DOCTYPE html>
<html lang="en">
<head>
<meta charset="utf-8">
<title>Marlowe Tenbury Design and Consulting, Inc. – Business Card</title>
<link rel="stylesheet" href="https://fonts.googleapis.com/css2?family=Arvo&family=Lato:wght@400&family=Montserrat:wght@600&display=swap">
<style>
  :root {
    --backdrop: #e9e5e1;
    --plum: #5c3b3d;
    --rose: #b85e5e;
    --paper: #f7f7f8;
    --ink: #111111;
    --white: #ffffff;
    --rule: #a89090;
  }
  * { margin: 0; padding: 0; box-sizing: border-box; }
  html, body {
    width: 1200px; height: 900px; overflow: hidden;
    background: var(--backdrop);
  }
  .canvas { position: relative; width: 1200px; height: 900px; }

  .card {
    position: absolute;
    box-shadow: 3px 4px 6px rgba(0,0,0,0.35);
  }
  .card-front {
    left: 330px; top: 90px; width: 555px; height: 343px;
    background: var(--plum); color: var(--white); text-align: center;
  }
  .card-back {
    left: 330px; top: 469px; width: 559px; height: 343px;
    background: var(--paper); text-align: center;
  }

  .owner-name {
    position: absolute; left: 0; right: 0; top: 88px;
    font-family: "Arvo", serif; font-size: 29px; letter-spacing: 0.2px;
    font-weight: 400; line-height: 1;
  }
  .owner-company {
    position: absolute; left: 0; right: 0; top: 122px;
    font-family: "Montserrat", sans-serif; font-weight: 600;
    font-size: 10px; letter-spacing: 2.2px; text-transform: uppercase;
  }
  .contact-divider {
    position: absolute; left: 188px; top: 157px; width: 179px; height: 22px;
  }
  .contact-list {
    position: absolute; left: 0; right: 0; top: 189px;
    list-style: none;
    font-family: "Lato", sans-serif; font-size: 16px; line-height: 20.5px;
  }

  .brand-mark {
    position: absolute; left: 0; right: 0; top: 155px;
    display: flex; align-items: center; justify-content: center; gap: 12px;
  }
  .brand-dot {
    width: 22px; height: 22px; border-radius: 50%; background: var(--rose);
  }
  .brand-name {
    font-family: "Arvo", serif; font-size: 28px; color: var(--plum); line-height: 1;
  }
  .tagline {
    position: absolute; left: 0; right: 0; top: 290px;
    font-family: "Lato", sans-serif; font-size: 16px; color: var(--ink);
    text-transform: uppercase; letter-spacing: 0.2px;
  }
</style>
</head>
<body>
<main class="canvas">
  <section class="card card-front">
    <h1 class="owner-name">Marlowe Tenbury</h1>
    <p class="owner-company">Design and Consulting, Inc.</p>
    <svg class="contact-divider" viewBox="0 0 179 22" aria-hidden="true">
      <line x1="0" y1="11" x2="52" y2="11" stroke="var(--rule)" stroke-width="1"/>
      <line x1="127" y1="11" x2="179" y2="11" stroke="var(--rule)" stroke-width="1"/>
      <g class="icon-phone">
        <circle cx="63" cy="11" r="10.5" fill="var(--white)"/>
        <path d="M57 9 q6 -5 12 0 l-1.5 2 h-2 l-0.5 -1.5 h-4 l-0.5 1.5 h-2 z M58.5 12 h9 l1 4 h-11 z" fill="var(--plum)"/>
      </g>
      <g class="icon-mail">
        <circle cx="89.5" cy="11" r="10.5" fill="var(--white)"/>
        <rect x="83" y="6.5" width="13" height="9" fill="none" stroke="var(--plum)" stroke-width="1.4"/>
        <path d="M83 6.5 l6.5 5 l6.5 -5" fill="none" stroke="var(--plum)" stroke-width="1.4"/>
      </g>
      <g class="icon-web">
        <circle cx="116" cy="11" r="10.5" fill="var(--white)"/>
        <circle cx="116" cy="11" r="6.5" fill="none" stroke="var(--plum)" stroke-width="1.4"/>
        <ellipse cx="116" cy="11" rx="2.8" ry="6.5" fill="none" stroke="var(--plum)" stroke-width="1.1"/>
        <line x1="109.5" y1="11" x2="122.5" y2="11" stroke="var(--plum)" stroke-width="1.1"/>
      </g>
    </svg>
    <ul class="contact-list">
      <li class="contact-phone">608-241-7789</li>
      <li class="contact-email">marlowe@mtvorplan.com</li>
      <li class="contact-web">www.mtvorplan.com</li>
    </ul>
  </section>

  <section class="card card-back">
    <div class="brand-mark">
      <span class="brand-dot" aria-hidden="true"></span>
      <span class="brand-name">Marlowe Tenbury</span>
    </div>
    <p class="tagline">Serving Kitchen &amp; Bath Business</p>
  </section>
</main>
</body>
</html>
```